Registry Program Flyer design 2 - MV Linkway registry

We need two different flyers that will be distributed via web, email and print. This project is for the second of the two flyers.

The audience is patients and family members of patients with a specific disease. The flyer will be used to make patients aware of our web-based registry programs, and to inform/encourage patients to join.

An example prototype flyer with the text that should be used is attached. We would like to improve the design and layout of the flyer, while retaining as much of the language as appropriate.

The MVLinkway flyer should use the logo provided in the example and a color scheme compatible with the logo. The flyer may use the pictures included in the prototype.

If possible, a final format that allows us to edit the text is preferred. If this is not possible, we will finalize the text after receiving a prototype. Changes to the text will likely be minor.

Note: The design of the flyers for this project and the other project (Registry Program Flyer Design 1 - TRBQ registry) can be similar in style, however, they should not be duplicates.

Deliverables will be a final .PSD (photoshop) file with layers so we can edit text if necessary.

Target Market(s)

Physicians and healthcare professionals.

Requirements
Must have
• Use the attached logo and colors.

```html
<!DOCTYPE html>
<html lang="en">
<head>
<meta charset="utf-8">
<title>MV Linkway Registry Flyer</title>
<link href="https://fonts.googleapis.com/css2?family=Open+Sans:ital,wght@0,400;0,600;0,700;1,400&display=swap" rel="stylesheet">
<style>
:root{
  --red:#d3262b;
  --red-deep:#9e1a1c;
  --charcoal:#2b2b2b;
  --slate:#5a5a5a;
  --white:#ffffff;
  --ink:#1e1e1e;
  --photo-a:#c9d3dc;
  --photo-b:#e9e2dc;
}
*{margin:0;padding:0;box-sizing:border-box}
html,body{width:1200px;height:927px;overflow:hidden;background:var(--white)}
body{font-family:"Open Sans",Arial,sans-serif;color:var(--white);position:relative}
.flyer{position:relative;width:1200px;height:927px}
.header-art{position:absolute;left:0;top:0}
.brand{position:absolute;left:58px;top:38px;color:var(--ink);display:flex;align-items:flex-start;gap:12px}
.brand-mark{width:52px;height:52px;background:var(--red);margin-top:4px}
.brand-name{font-size:34px;line-height:38px;font-weight:400}
.brand-name small{display:block;font-size:22px;line-height:28px}
.join-tag{position:absolute;left:430px;top:150px;width:170px;text-align:center;transform:rotate(45deg);transform-origin:center;font-weight:700;letter-spacing:2px;font-size:15px;line-height:19px}
.join-tag .url{font-weight:400;font-size:16px;letter-spacing:1.5px}
.panel-dark{position:absolute;left:0;top:258px;width:575px;height:562px;background:linear-gradient(135deg,var(--slate),var(--charcoal))}
.panel-red{position:absolute;left:575px;top:258px;width:625px;height:562px;background:linear-gradient(135deg,var(--red),var(--red-deep))}
.side{position:absolute;left:52px;top:14px;width:508px;font-size:14.5px;letter-spacing:1.4px;line-height:20px}
.side h3{font-size:15px;font-weight:400;text-align:right;letter-spacing:1.6px;margin:0 0 14px}
.side h3 b{font-weight:700}
.who-list{list-style:none;text-align:right;margin-bottom:26px}
.who-list li::after{content:"";display:inline-block;width:7px;height:7px;border-radius:50%;background:var(--white);margin-left:10px;vertical-align:middle}
.side p{text-align:justify;text-align-last:right;margin-bottom:20px}
.main{position:absolute;left:22px;top:10px;width:556px;font-size:14.5px;letter-spacing:1.4px;line-height:20px}
.main h2{font-size:25px;font-weight:400;letter-spacing:1.5px;margin-bottom:16px}
.main h2 b,.main h4 b{font-weight:700}
.main p{text-align:justify;margin-bottom:22px}
.main h4{font-size:19px;font-weight:400;letter-spacing:1px;margin-bottom:14px}
.benefits{list-style:none;font-style:italic;margin-bottom:22px}
.benefits li{position:relative;padding-left:26px;width:500px}
.benefits li::before{content:"";position:absolute;left:2px;top:6px;width:7px;height:7px;border-radius:50%;background:var(--white)}
.tagline{position:absolute;left:0;top:830px;width:1200px;text-align:center;color:var(--red);font-weight:700;font-size:16.5px;letter-spacing:2.2px}
.partners{position:absolute;left:258px;top:862px;display:flex;align-items:center;gap:14px;color:var(--ink)}
.partner-name{display:flex;align-items:center;gap:6px;font-size:13px;line-height:14px}
.partner-name i{width:14px;height:14px;background:var(--red);display:block}
.badge{width:56px;height:44px;border-radius:50%;background:#d9dbe6}
.badge.square{border-radius:4px;width:58px;height:34px;background:#bfe0f0}
.sponsor{font-size:12px;margin-left:8px;letter-spacing:.5px}
.sponsor-name{font-size:20px;color:var(--red-deep);margin-left:4px}
</style>
</head>
<body>
<div class="flyer">
  <svg class="header-art" width="1200" height="258" viewBox="0 0 1200 258">
    <defs>
      <linearGradient id="photoTone" x1="0" y1="0" x2="0" y2="1">
        <stop offset="0" stop-color="var(--photo-a)"/>
        <stop offset="1" stop-color="var(--photo-b)"/>
      </linearGradient>
    </defs>
    <polygon points="425,100 555,100 575,118 575,258 425,258 482,182" fill="var(--red)"/>
    <polygon role="img" aria-label="Photo of three smiling women in white tops standing together" points="575,28 705,28 745,0 745,140 800,198 745,198 745,258 575,258" fill="url(#photoTone)"/>
  </svg>

  <div class="brand">
    <span class="brand-mark"></span>
    <div class="brand-name">MV Linkway<small>Registry</small></div>
  </div>

  <div class="join-tag">JOIN<br><span class="url">mvlinkway.org</span><br>TODAY!</div>

  <section class="panel-dark">
    <div class="side">
      <h3>WHO CAN <b>PARTICIPATE</b></h3>
      <ul class="who-list">
        <li>Patients</li>
        <li>Family members</li>
        <li>Healthcare providers</li>
        <li>Investigators &amp; researchers</li>
        <li>All stakeholders interested in TRBQ</li>
      </ul>
      <h3>HOW IT <b>WORKS</b></h3>
      <p>Patients can join the registry to submit their data. After taking web-based surveys, explore the collected information in a way that protects the privacy of everyone.</p>
      <h3>WHO <b>WE ARE</b></h3>
      <p>As its name implies, MV Linkway represents the coming together of a wide range of entities and individuals who recognize the value in pooling their combined expertise and information. The Governing Board of MV Linkway comes from leaders in the non-profit sector, government agencies and academic institutions.</p>
      <p>Regardless of their individual backgrounds, the thought leaders of MV Linkway share a common goal to increase the community’s ability to help one another through improved communication, and by doing so, to help the millions of people affected by Lipodystrophy.</p>
    </div>
  </section>

  <section class="panel-red">
    <div class="main">
      <h2>GET <b>CONNECTED.</b></h2>
      <p>One of the most important steps towards finding effective treatments for lipodystrophy (LD) is to uncover the ways in which the diseases behave, the symptoms that are commonly seen and how those symptoms progress. This requires the collection of as much information as possible about all people affected by LD. MV Linkway will serve as that database–the critical link between the patient community and the scientific community. The more people who join the registry the greater the chances that research will produce results that benefit everyone.</p>
      <h4>Join <b>THE LINKWAY TRBQ</b> Registry to:</h4>
      <ul class="benefits">
        <li>Tell us about your experience with LD and learn about the experiences with others</li>
        <li>Share information in a program that protects your privacy</li>
        <li>Provide valuable quality-of-life information that can be used to advocate on behalf of the LD community</li>
        <li>Help the research community launch clinical trials and studies</li>
      </ul>
      <p>We need to hear YOUR VOICE and we hope you will decide to join MV Linkway. Every individual who joins makes a vital contribution toward helping all of those affected by lipodystrophy.</p>
    </div>
  </section>

  <div class="tagline">YOUR INFORMATION WILL LEAD TO FUTURE TREATMENTS AND CURES FOR ALL TYPES OF LIPODYSTROPHY</div>

  <div class="partners">
    <span class="partner-name"><i></i>Kinfold<br>United</span>
    <span class="badge"></span>
    <span class="badge"></span>
    <span class="badge square"></span>
    <span class="sponsor">Sponsored by:</span>
    <span class="sponsor-name">Norvale Pharma</span>
  </div>
</div>
</body>
</html>
```